Vorminta - Plastic to Diesel Energy Needs A Website

Make website explaining the concept and the team behind the company
Updates

I will be providing A logo and Information about the company upon signed NDA.

Coding

Coded - Design and coding required

Number of Pages Required

5+ page

```html
<!DOCTYPE html>
<html lang="en">
<head>
<meta charset="utf-8">
<title>Vorminta – Plastic to Diesel Energy</title>
<link href="https://fonts.googleapis.com/css2?family=Krona+One&family=Outfit:wght@300;400;500;600&display=swap" rel="stylesheet">
<style>
:root{
  --green:#8cc63f;
  --green-dark:#6fa82a;
  --blue:#1b9ad6;
  --blue-deep:#0a7dbf;
  --ink:#111214;
  --dark:#0c0d0f;
  --text:#4a4d52;
  --muted:#8a8d92;
  --light:#f1f1f1;
  --white:#ffffff;
}
*{box-sizing:border-box;margin:0;padding:0}
html,body{width:1200px;height:4918px;overflow:hidden}
body{font-family:'Outfit',sans-serif;color:var(--text);background:var(--white);position:relative}
.display{font-family:'Krona One',sans-serif;text-transform:uppercase;color:var(--ink);letter-spacing:.02em}
section,header,footer{position:absolute;left:0;width:1200px;overflow:hidden}
.abs{position:absolute}
.fill{position:absolute;inset:0}
.btn{position:absolute;display:flex;align-items:center;background:var(--green);color:var(--white);font-size:9px;font-weight:600;text-transform:uppercase;letter-spacing:.04em;padding-left:24px}
.btn .arrow{position:absolute;right:4px;top:4px;bottom:4px;width:26px;background:var(--white);display:flex;align-items:center;justify-content:center}
.centered{text-align:center;left:0;right:0}

/* hero */
.hero{top:0;height:601px}
.hero .bg{background:radial-gradient(ellipse at 78% 30%,#c98a4a 0%,#7a5230 22%,#2e2a24 52%,#14181a 80%)}
.hero .shade{background:linear-gradient(90deg,rgba(0,0,0,.55) 0%,rgba(0,0,0,.2) 55%,rgba(0,0,0,.1) 100%)}
.brand{position:absolute;display:flex;align-items:center;gap:8px}
.brand-dot{width:14px;height:14px;border-radius:50%;background:var(--green)}
.brand-name{font-family:'Krona One',sans-serif;color:var(--blue);font-size:22px;letter-spacing:.02em}
.brand-tag{position:absolute;font-size:9.5px;font-weight:600;color:var(--green);letter-spacing:.02em;text-transform:uppercase}
.nav a{position:absolute;top:35px;font-size:9px;font-weight:500;color:var(--white);text-decoration:none;text-transform:uppercase}
.nav a.active{color:var(--green)}
.hero-title{left:124px;top:368px;font-size:34px;line-height:38px;color:var(--white)}
.counter{left:124px;top:548px;color:var(--white);font-size:32px;font-weight:500}
.counter small{font-size:12px;opacity:.8}
.hero-rule{left:124px;top:584px;width:950px;height:1px;background:rgba(255,255,255,.3)}

/* about */
.about-title{top:656px;font-size:28px}
.about-band{top:748px;height:540px;background:var(--dark)}
.about-band .glow{left:0;top:0;width:736px;height:540px;background:radial-gradient(ellipse at 62% 8%,#6a3d14 0%,#2a1a0c 30%,#0c0d0f 65%)}
.about-band .photo{left:736px;top:0;width:464px;height:540px;background:linear-gradient(180deg,#6c7886 0%,#9aa3ab 40%,#8b8d87 70%,#5b5a52 100%)}
.about-band h3{left:124px;top:124px;font-size:17px;line-height:23px;color:var(--white)}
.about-band p{left:124px;width:420px;font-size:10.5px;line-height:15px;color:#cfd1d4}
.stat{top:400px;color:var(--white)}
.stat b{font-family:'Outfit',sans-serif;font-weight:600;font-size:32px}
.stat sup{font-size:12px;margin-left:3px}
.stat span{display:block;margin-top:20px;font-size:9.5px;color:#bfc2c6}

/* process */
.process-title{top:1400px;font-size:24px;line-height:32px}
.step{top:1505px;width:211px;height:273px;background:var(--white);box-shadow:0 6px 24px rgba(0,0,0,.08);padding:46px 30px 0 30px}
.step.featured{top:1486px;height:309px;background:linear-gradient(180deg,var(--blue) 0%,#1790cc 65%,#0d6ea8 100%);box-shadow:none;padding-top:64px}
.step svg{display:block;margin:0 0 28px 22px}
.step h4{font-family:'Krona One',sans-serif;font-size:11.5px;line-height:15px;text-transform:uppercase;color:var(--ink);font-weight:400}
.step p{margin-top:14px;font-size:10px;line-height:15px;color:var(--muted)}
.step.featured h4,.step.featured p{color:var(--white)}

/* impact */
.impact{top:1900px;height:575px;background:#050608}
.impact .bg{background:linear-gradient(180deg,#050608 0%,#0b0d12 45%,#28251f 75%,#3b2f1f 88%,#15120e 100%)}
.impact h2{top:104px;font-size:24px;line-height:32px;color:var(--white)}
.impact p{top:170px;font-size:10.5px;line-height:16px;color:#d4d6da}
.ring{width:150px;height:150px;border-radius:50%;border:1px solid rgba(255,255,255,.22);display:flex;align-items:center;justify-content:center;text-align:center;font-size:10.5px;line-height:15px;color:var(--white);top:229px}
.ring-dot{width:5px;height:5px;border-radius:50%;background:var(--green);top:302px}

/* markets */
.markets-title{left:124px;top:2578px;font-size:24px;line-height:31px}
.tab{top:2592px;font-size:10px;line-height:15px;color:var(--text)}
.tab.active{color:var(--blue)}
.tab-rule{left:593px;top:2634px;width:481px;height:1px;background:#e0e0e0}
.tab-mark{left:710px;top:2633px;width:73px;height:3px;background:var(--blue)}
.market-photo{left:124px;top:2704px;width:492px;height:362px;background:linear-gradient(150deg,#e0642a 0%,#c65826 25%,#6d7275 50%,#4a4f52 100%)}
.market-card{left:672px;top:2704px;width:402px;height:274px;background:var(--light);padding:52px 38px 0 44px}
.market-card h3{font-size:18px;line-height:22px}
.market-card p{margin-top:16px;font-size:10.2px;line-height:15px;color:var(--text)}
.square-btn{width:42px;height:40px;background:var(--green);display:flex;align-items:center;justify-content:center}

/* values */
.values{top:3171px;height:506px}
.values .bg{background:linear-gradient(180deg,#2b3035 0%,#464a48 40%,#5a5850 70%,#3a3a36 100%)}
.values .shade{background:rgba(10,12,14,.35)}
.values h2{top:130px;font-size:28px;line-height:32px;color:var(--white)}
.value{top:220px;width:164px;height:164px;border-radius:50%;background:var(--white);border:5px solid rgba(255,255,255,.35);background-clip:padding-box;text-align:center;font-size:10.5px;line-height:14px;color:var(--text);padding-top:38px}
.value svg{display:block;margin:0 auto 14px}

/* team */
.team-title{top:3775px;font-size:26px;line-height:32px}
.team-intro{top:3850px;font-size:10.5px;line-height:16px;color:var(--text)}
.member{top:3902px;height:343px;background:linear-gradient(180deg,#e8e8e8 0%,#d7d7d7 100%)}
.member .plate{position:absolute;left:17px;right:17px;top:267px;height:48px;background:var(--white);text-align:center;padding-top:11px}
.member h5{font-family:'Krona One',sans-serif;font-size:11px;color:var(--ink);text-transform:uppercase;font-weight:400}
.member span{font-size:8.5px;color:var(--muted)}
.dot{top:4284px;width:7px;height:7px;border-radius:50%;background:var(--ink)}

/* partner */
.partner{top:4373px;height:182px;background:linear-gradient(90deg,#1aa3de 0%,#1691cf 60%,#0f78b5 100%)}
.partner .truck{left:740px;top:0;width:300px;height:182px;background:radial-gradient(ellipse at 50% 60%,rgba(160,220,250,.55) 0%,rgba(27,154,214,0) 70%)}
.partner h2{left:124px;top:74px;font-size:24px;line-height:32px;color:var(--white)}
.partner .btn{background:var(--white);color:var(--ink);left:891px;top:76px;width:183px;height:33px}
.partner .btn .arrow{background:var(--green)}

/* footer */
.site-footer{top:4555px;height:363px;background:var(--ink);color:#d9dbde}
.site-footer h6{position:absolute;top:106px;font-family:'Krona One',sans-serif;font-size:12.5px;color:var(--green);font-weight:400;text-transform:uppercase}
.links{position:absolute;left:471px;top:134px;list-style:none;font-size:10px;line-height:21.5px;color:#e6e6e6}
.links li::before{content:"›";margin-right:6px}
.contact{position:absolute;left:666px;font-size:10px;line-height:14px}
.contact b{font-weight:600;color:var(--white)}
.social{position:absolute;top:165px;width:27px;height:27px;border:1px solid rgba(255,255,255,.3);display:flex;align-items:center;justify-content:center}
.social i{width:7px;height:7px;background:#e6e6e6;display:block}
.footer-rule{left:124px;top:320px;width:950px;height:1px;background:rgba(255,255,255,.12)}
.copyright{top:331px;font-size:9.5px;color:#cfd1d4}
.to-top{left:1120px;top:301px;width:32px;height:32px;background:var(--green);display:flex;align-items:center;justify-content:center}
</style>
</head>
<body>

<header class="hero">
  <div class="fill bg" role="img" aria-label="Close-up of hands crushing a clear plastic bottle in warm light"></div>
  <div class="fill shade"></div>
  <div class="brand" style="left:124px;top:24px"><span class="brand-dot"></span><span class="brand-name">Vorminta</span></div>
  <div class="brand-tag" style="left:124px;top:54px">Plastic to Diesel Energy</div>
  <nav class="nav">
    <a class="active" style="left:382px">Home</a>
    <a style="left:437px">About</a>
    <a style="left:494px">Technology</a>
    <a style="left:583px">Environmental Impact</a>
    <a style="left:721px">Team</a>
    <a style="left:771px">Contact</a>
  </nav>
  <a class="btn" style="left:889px;top:25px;width:185px;height:36px">Request Partnership<span class="arrow"><svg width="8" height="8" viewBox="0 0 8 8"><path d="M2 1l3 3-3 3" stroke="#111" stroke-width="1.4" fill="none"/></svg></span></a>
  <h1 class="abs display hero-title">Turning Plastic<br>Waste Into Clean<br>Diesel Energy</h1>
  <a class="btn" style="left:889px;top:408px;width:185px;height:35px">Learn Our Process<span class="arrow"><svg width="8" height="8" viewBox="0 0 8 8"><path d="M2 1l3 3-3 3" stroke="#111" stroke-width="1.4" fill="none"/></svg></span></a>
  <div class="abs counter">1<small> / 3</small></div>
  <svg class="abs" style="left:591px;top:550px" width="16" height="24" viewBox="0 0 16 24"><rect x="1" y="1" width="14" height="22" rx="7" stroke="#fff" stroke-opacity=".7" fill="none"/><line x1="8" y1="6" x2="8" y2="10" stroke="#fff"/></svg>
  <svg class="abs" style="left:1009px;top:556px" width="16" height="12" viewBox="0 0 16 12"><path d="M8 2L4 6l4 4M13 2L9 6l4 4" stroke="#fff" stroke-opacity=".75" fill="none" stroke-width="1.2"/></svg>
  <div class="abs" style="left:1043px;top:548px;width:1px;height:28px;background:rgba(255,255,255,.3)"></div>
  <svg class="abs" style="left:1060px;top:556px" width="16" height="12" viewBox="0 0 16 12"><path d="M3 2l4 4-4 4M8 2l4 4-4 4" stroke="#fff" stroke-opacity=".75" fill="none" stroke-width="1.2"/></svg>
  <div class="abs hero-rule"></div>
</header>

<h2 class="abs display centered about-title">About Vorminta</h2>

<section class="about-band">
  <div class="abs glow" role="img" aria-label="Amber droplets of fuel on a dark surface"></div>
  <div class="abs photo" role="img" aria-label="Refinery tower with a gas flare and yellow stair railings"></div>
  <h3 class="abs display">A Smarter Solution<br>For Plastic Waste</h3>
  <p class="abs" style="top:178px">Plastic waste is one of the biggest environmental challenges of our time. At Vorminta, we use advanced conversion technology to transform discarded plastic into usable diesel fuel.</p>
  <p class="abs" style="top:238px">Our mission is simple: reduce global plastic pollution while producing reliable fuel for commercial industries. By turning waste into energy, we help businesses operate efficiently while contributing to a cleaner planet.</p>
  <a class="btn" style="left:124px;top:315px;width:162px;height:36px">Find Out More<span class="arrow"><svg width="8" height="8" viewBox="0 0 8 8"><path d="M2 1l3 3-3 3" stroke="#111" stroke-width="1.4" fill="none"/></svg></span></a>
  <div class="abs stat" style="left:124px"><b>4</b><sup>+</sup><span>Certification and Qualification</span></div>
  <div class="abs stat" style="left:292px"><b>10</b><sup>+</sup><span>Flexible Recycling Solutions</span></div>
  <div class="abs stat" style="left:450px"><b>15</b><sup>+</sup><span>Inventions Patented Technologies</span></div>
  <div class="abs stat" style="left:633px"><b>50</b><sup>+</sup><span>Successful Cases</span></div>
</section>

<h2 class="abs display centered process-title">From Plastic Waste<br>To Diesel Fuel</h2>

<article class="abs step" style="left:179px">
  <svg width="56" height="60" viewBox="0 0 56 60" fill="none" stroke="#111" stroke-width="2"><rect x="6" y="14" width="14" height="40" rx="3"/><path d="M10 14V6h6v8"/><circle cx="30" cy="32" r="10" stroke="#8cc63f"/><rect x="38" y="20" width="12" height="34" rx="2"/></svg>
  <h4>1. Plastic<br>Collection</h4>
  <p>We collect non-recyclable plastic waste from industrial and municipal sources.</p>
</article>
<article class="abs step" style="left:390px">
  <svg width="56" height="60" viewBox="0 0 56 60" fill="none" stroke="#111" stroke-width="2"><rect x="4" y="8" width="42" height="40" rx="3"/><line x1="4" y1="18" x2="46" y2="18"/><rect x="12" y="26" width="14" height="14"/><circle cx="42" cy="44" r="9" stroke="#8cc63f"/></svg>
  <h4>2. Advanced<br>Conversion</h4>
  <p>Through a specialized thermal conversion process, plastic is broken down.</p>
</article>
<article class="abs step featured" style="left:601px">
  <svg width="56" height="60" viewBox="0 0 56 60" fill="none" stroke="#fff" stroke-width="2"><path d="M24 4h10v8H24z"/><rect x="18" y="12" width="30" height="42" rx="3"/><rect x="6" y="26" width="20" height="28" rx="2"/><line x1="11" y1="36" x2="21" y2="36"/><line x1="11" y1="43" x2="21" y2="43"/></svg>
  <h4>3. Diesel<br>Refinement</h4>
  <p>The output fuel is refined into high-quality diesel suitable for commercial use.</p>
</article>
<article class="abs step" style="left:812px">
  <svg width="60" height="60" viewBox="0 0 60 60" fill="none" stroke="#111" stroke-width="2"><rect x="8" y="10" width="16" height="12"/><rect x="36" y="10" width="16" height="12"/><path d="M30 22v10M16 22l14 10 14-10"/><rect x="18" y="34" width="24" height="14" stroke="#8cc63f"/><circle cx="22" cy="52" r="3"/><circle cx="38" cy="52" r="3"/></svg>
  <h4>4. Commercial<br>Supply</h4>
  <p>The diesel produced is supplied to industries that rely on dependable fuel sources.</p>
</article>

<section class="impact">
  <div class="fill bg" role="img" aria-label="Industrial refinery skyline lit at night with smoke stacks"></div>
  <h2 class="abs display centered">Reducing Plastic Pollution,<br>Powering Industries</h2>
  <p class="abs centered">Every year, millions of tons of plastic waste end up in landfills and oceans. Vorminta's technology provides<br>a sustainable alternative by converting waste plastic into usable fuel.</p>
  <div class="abs ring" style="left:238px">Reduces<br>plastic waste<br>pollution</div>
  <div class="abs ring" style="left:429px">Supports circular<br>economy<br>solutions</div>
  <div class="abs ring" style="left:621px">Produces<br>alternative diesel<br>fuel</div>
  <div class="abs ring" style="left:812px">Decreases<br>environmental<br>impact of waste</div>
  <span class="abs ring-dot" style="left:236px"></span>
  <span class="abs ring-dot" style="left:386px"></span>
  <span class="abs ring-dot" style="left:578px"></span>
  <span class="abs ring-dot" style="left:769px"></span>
  <span class="abs ring-dot" style="left:960px"></span>
</section>

<h2 class="abs display markets-title">Reliable Diesel<br>For Commercial<br>Operations</h2>
<div class="abs tab" style="left:593px">Transportation &amp;<br>Logistics</div>
<div class="abs tab active" style="left:712px">Construction<br>Companies</div>
<div class="abs tab" style="left:812px">Manufacturing<br>Facilities</div>
<div class="abs tab" style="left:918px">Agricultural<br>Operations</div>
<div class="abs tab" style="left:1018px">Industrial<br>Generators</div>
<div class="abs tab-rule"></div>
<div class="abs tab-mark"></div>
<div class="abs market-photo" role="img" aria-label="Aerial view of a forklift moving fuel barrels beside stacks of orange drums"></div>
<div class="abs market-card">
  <h3 class="display">Construction<br>Companies</h3>
  <p>Vorminta provides reliable diesel fuel solutions for construction companies, ensuring uninterrupted operations on-site. Our diesel, produced from recycled plastic, helps reduce environmental impact while powering machinery, generators, and vehicles efficiently. Partnering with Vorminta means your projects stay on schedule with sustainable, high-quality fuel.</p>
</div>
<div class="abs square-btn" style="left:971px;top:2959px"><svg width="10" height="10" viewBox="0 0 10 10"><path d="M3 1l4 4-4 4" stroke="#fff" stroke-width="1.6" fill="none"/></svg></div>
<svg class="abs" style="left:672px;top:3020px" width="150" height="12" viewBox="0 0 150 12" fill="none" stroke="#b5b5b5"><path d="M0 6h68M5 2L1 6l4 4"/><path d="M82 6h68M145 2l4 4-4 4"/></svg>

<section class="values">
  <div class="fill bg" role="img" aria-label="Recycling facility with bales of compressed plastic and a conveyor belt"></div>
  <div class="fill shade"></div>
  <h2 class="abs display centered">Innovative Fuel.<br>Sustainable Future.</h2>
  <div class="abs value" style="left:225px"><svg width="28" height="28" viewBox="0 0 28 28"><circle cx="14" cy="14" r="12" fill="none" stroke="#1b9ad6" stroke-width="2"/><path d="M8.5 14.5l3.5 3.5 7-8" stroke="#1b9ad6" stroke-width="2.2" fill="none"/></svg>Advanced<br>plastic-to-diesel<br>technology</div>
  <div class="abs value" style="left:422px"><svg width="28" height="28" viewBox="0 0 28 28"><circle cx="14" cy="14" r="12" fill="none" stroke="#1b9ad6" stroke-width="2"/><path d="M8.5 14.5l3.5 3.5 7-8" stroke="#1b9ad6" stroke-width="2.2" fill="none"/></svg>Environmentally<br>responsible fuel<br>production</div>
  <div class="abs value" style="left:616px"><svg width="28" height="28" viewBox="0 0 28 28"><circle cx="14" cy="14" r="12" fill="none" stroke="#1b9ad6" stroke-width="2"/><path d="M8.5 14.5l3.5 3.5 7-8" stroke="#1b9ad6" stroke-width="2.2" fill="none"/></svg>Reliable<br>commercial fuel<br>supply</div>
  <div class="abs value" style="left:807px"><svg width="28" height="28" viewBox="0 0 28 28"><circle cx="14" cy="14" r="12" fill="none" stroke="#1b9ad6" stroke-width="2"/><path d="M8.5 14.5l3.5 3.5 7-8" stroke="#1b9ad6" stroke-width="2.2" fill="none"/></svg>Commitment to<br>sustainability and<br>innovation</div>
</section>

<h2 class="abs display centered team-title">Experts In Energy And<br>Environmental Innovation</h2>
<p class="abs centered team-intro">Vorminta is powered by a team of engineers, environmental specialists, and energy professionals<br>committed to solving the global plastic waste crisis.</p>
<div class="abs member" style="left:177px;width:273px" role="img" aria-label="Portrait of a team member in a yellow hard hat and safety vest">
  <div class="plate"><h5>Marla Oyelaran</h5><span>Assistant</span></div>
</div>
<div class="abs member" style="left:466px;width:271px" role="img" aria-label="Portrait of a team member in an orange hard hat holding a clipboard">
  <div class="plate"><h5>Teodor Vasquel</h5><span>Admin, Partner</span></div>
</div>
<div class="abs member" style="left:752px;width:271px" role="img" aria-label="Portrait of a team member in an orange hard hat and work overalls">
  <div class="plate"><h5>Idris Kallenberg</h5><span>Co-Ordinator</span></div>
</div>
<span class="abs dot" style="left:582px"></span>
<span class="abs dot" style="left:597px;background:var(--green)"></span>
<span class="abs dot" style="left:612px"></span>

<section class="partner">
  <div class="abs truck" role="img" aria-label="Blue-toned semi truck hauling a fuel tanker"></div>
  <h2 class="abs display">Partner With Us For<br>Sustainable Fuel Solutions</h2>
  <a class="btn">Become A Partner<span class="arrow"><svg width="8" height="8" viewBox="0 0 8 8"><path d="M2 1l3 3-3 3" stroke="#fff" stroke-width="1.4" fill="none"/></svg></span></a>
</section>

<footer class="site-footer">
  <div class="brand" style="left:191px;top:122px"><span class="brand-dot" style="width:18px;height:18px"></span><span class="brand-name" style="font-size:28px">Vorminta</span></div>
  <div class="brand-tag" style="left:191px;top:162px;font-size:12px">Plastic to Diesel Energy</div>

  <h6 style="left:471px">Quick Links</h6>
  <ul class="links"><li>Home</li><li>About</li><li>Technology</li><li>Sustainability</li><li>Contact</li></ul>

  <h6 style="left:666px">Contact Us</h6>
  <svg class="abs" style="left:666px;top:136px" width="10" height="10" viewBox="0 0 10 10"><path d="M2 1l2 0 1 2-1 1a6 6 0 0 0 2 2l1-1 2 1v2c-4 0-7-3-7-7z" fill="#e6e6e6"/></svg>
  <div class="contact" style="top:133px;padding-left:20px"><b>Call Us:</b><br>+1 000 000 0000</div>
  <svg class="abs" style="left:666px;top:172px" width="10" height="8" viewBox="0 0 10 8"><rect width="10" height="8" fill="#e6e6e6"/><path d="M0 0l5 4 5-4" stroke="#111" fill="none"/></svg>
  <div class="contact" style="top:169px;padding-left:20px"><b>Email Address:</b><br>info@vorminta.com</div>
  <svg class="abs" style="left:667px;top:206px" width="8" height="11" viewBox="0 0 8 11"><path d="M4 0a4 4 0 0 1 4 4c0 3-4 7-4 7S0 7 0 4a4 4 0 0 1 4-4z" fill="#e6e6e6"/><circle cx="4" cy="4" r="1.5" fill="#111"/></svg>
  <div class="contact" style="top:203px;padding-left:20px"><b>Location</b><br>Some Goes Address Link here</div>

  <h6 style="left:859px">Follow Us</h6>
  <div class="contact" style="left:865px;top:136px;font-size:9.5px">Check Us Out on Social Media!</div>
  <span class="social" style="left:865px"><i></i></span>
  <span class="social" style="left:899px"><i></i></span>
  <span class="social" style="left:933px"><i></i></span>
  <span class="social" style="left:967px"><i></i></span>

  <div class="abs footer-rule"></div>
  <div class="abs centered copyright">Copyright © 2026 Vorminta. All rights reserved.</div>
  <div class="abs to-top"><svg width="10" height="12" viewBox="0 0 10 12"><path d="M5 11V1M1 5l4-4 4 4" stroke="#fff" stroke-width="1.4" fill="none"/></svg></div>
</footer>

</body>
</html>
```